Flyer-Design für Physiotherapie-Praxis
Zielgruppe
Wir sind eine Praxis für Physiotherapie und möchten durch diesen Flyer neue Patienten werben. Der Flyer soll in Arztpraxen ausliegen und dort den Patienten direkt ansprechen und auf uns aufmerksam machen. Es ist auch eine Verknüpfung der Therapie mit einem Training in einem Gesundheitsstudio möglich, da im gleichen Haus das Kraftwerk Sonnhalde Lindmoos beheimatet ist.
Aufgabenstellung
Der Fokus auf unsere Prinzipien (Ganzheitliche Therapie, hohes Maß an Therapiemöglichkeiten, Variation in den therapeutischen Ansätzen durch unterschiedlich fortgebildete Therapeuten, die nach den gleichen Idealen arbeiten)

```html
<!DOCTYPE html>
<html lang="de">
<head>
<meta charset="utf-8">
<title>Flyer – Zentrum für Therapie &amp; Training</title>
<link href="https://fonts.googleapis.com/css2?family=Exo+2:wght@300;400;600;700&display=swap" rel="stylesheet">
<style>
  :root {
    --page-bg: #eeeff1;
    --paper: #ffffff;
    --brand-blue: #1a93c9;
    --brand-light: #2c9bd3;
    --brand-navy: #2b2d6e;
    --text-light: #ffffff;
    --muted: #8a8d94;
    --bar-dark: #c9ccd2;
    --bar-light: rgba(255,255,255,0.75);
  }
  * { margin: 0; padding: 0; box-sizing: border-box; }
  html, body {
    width: 1200px;
    height: 835px;
    overflow: hidden;
    background: var(--page-bg);
    font-family: "Exo 2", sans-serif;
  }

  /* viewer arrows */
  .nav-arrow {
    position: absolute;
    top: 360px;
    width: 22px;
    height: 22px;
  }
  .nav-arrow.prev { left: 110px; }
  .nav-arrow.next { left: 1082px; }
  .nav-arrow circle { fill: none; stroke: #9a9ca2; stroke-width: 0.8; }
  .nav-arrow.next circle { stroke: #45474d; }
  .nav-arrow path { fill: none; stroke: #9a9ca2; stroke-width: 1; }
  .nav-arrow.next path { stroke: #45474d; }

  /* main front panel */
  .flyer-panel {
    position: absolute;
    left: 457px;
    top: 48px;
    width: 308px;
    height: 647px;
    background: var(--paper);
    box-shadow: 0 1px 4px rgba(0,0,0,0.18);
    overflow: hidden;
  }
  .brand-mark {
    position: absolute;
    left: 111px;
    top: 40px;
    width: 86px;
    height: 86px;
    border: 2px solid var(--brand-blue);
    border-radius: 50%;
  }
  .brand-name {
    position: absolute;
    left: 0;
    top: 141px;
    width: 100%;
    text-align: center;
  }
  .brand-name .tagline {
    font-size: 13.6px;
    line-height: 18px;
    font-weight: 400;
    color: var(--brand-light);
    letter-spacing: 0.1px;
  }
  .brand-name .owners {
    font-size: 20px;
    line-height: 22px;
    font-weight: 600;
    color: var(--brand-navy);
  }
  .brand-name .holder {
    font-size: 13px;
    line-height: 18px;
    font-weight: 400;
    color: var(--brand-light);
  }
  .wave-band {
    position: absolute;
    left: 0;
    top: 0;
    width: 308px;
    height: 647px;
  }
  .wave-band path { fill: var(--brand-blue); }
  .intro {
    position: absolute;
    left: 27px;
    top: 286px;
    width: 276px;
    color: var(--text-light);
  }
  .intro h1 {
    font-weight: 300;
    font-size: 19px;
    line-height: 21px;
    letter-spacing: 0.2px;
    margin-bottom: 17px;
  }
  .intro h1 strong { font-weight: 700; }
  .intro p {
    font-weight: 300;
    font-size: 12.4px;
    line-height: 15.6px;
    margin-bottom: 15.6px;
  }
  .intro strong { font-weight: 600; }

  /* thumbnail strip */
  .thumb-strip {
    position: absolute;
    left: 474px;
    top: 723px;
    width: 266px;
    height: 93px;
  }
  .thumb {
    position: absolute;
    top: 0;
    height: 93px;
    overflow: hidden;
    background: var(--paper);
  }
  .thumb.blue { background: var(--brand-blue); }
  .thumb h3 {
    position: absolute;
    left: 2px;
    top: 7px;
    width: 40px;
    font-size: 3.3px;
    line-height: 4.2px;
    font-weight: 700;
    color: var(--text-light);
  }
  .thumb.white h3 { color: var(--brand-blue); }
  .lines {
    position: absolute;
    left: 2px;
    width: 38px;
  }
  .lines i {
    display: block;
    height: 1px;
    margin-bottom: 1.6px;
    background: var(--bar-light);
  }
  .thumb.white .lines i { background: var(--bar-dark); }
  .lines i.short { width: 65%; }
  .photo { position: absolute; }
  .photo.pool {
    left: 7px; top: 60px; width: 44px; height: 44px; border-radius: 50%;
    background: linear-gradient(180deg, #d7dde3 0%, #7c8f9e 50%, #2b7fbf 100%);
  }
  .photo.team {
    left: 1px; top: 34px; width: 41px; height: 29px;
    background: linear-gradient(180deg, #8fb3cf 0%, #b9cfe0 55%, #6f8aa3 100%);
  }
  .photo.gym {
    left: 8px; top: 55px; width: 44px; height: 44px; border-radius: 50%;
    background: linear-gradient(180deg, #dfe2e6 0%, #9ea5ad 55%, #4b535c 100%);
  }
  .mini-mark {
    position: absolute;
    width: 11px; height: 11px;
    border: 0.6px solid var(--brand-blue);
    border-radius: 50%;
  }
  .mini-mark.faint { border-color: #b9bcc2; }
  .mini-name {
    position: absolute;
    left: 0; width: 44px;
    text-align: center;
    font-size: 2.4px;
    line-height: 3px;
    color: var(--brand-navy);
  }
  .front-band {
    position: absolute;
    left: 0; top: 37px; width: 45px; height: 56px;
    background: var(--brand-blue);
  }
  .strip-label {
    position: absolute;
    top: 817px;
    font-size: 6.5px;
    color: var(--muted);
    letter-spacing: 0.2px;
  }
</style>
</head>
<body>
  <svg class="nav-arrow prev" viewBox="0 0 22 22" aria-label="Vorherige Seite">
    <circle cx="11" cy="11" r="10.5"/><path d="M12.5 7 L9 11 L12.5 15"/>
  </svg>
  <svg class="nav-arrow next" viewBox="0 0 22 22" aria-label="Nächste Seite">
    <circle cx="11" cy="11" r="10.5"/><path d="M9.5 7 L13 11 L9.5 15"/>
  </svg>

  <section class="flyer-panel">
    <div class="brand-mark"></div>
    <div class="brand-name">
      <div class="tagline">ZENTRUM FÜR THERAPIE &amp; TRAINING</div>
      <div class="owners">Lena Vogt &amp; Tobias Kern</div>
      <div class="holder">Inhaber: Tobias Kern</div>
    </div>

    <svg class="wave-band" viewBox="0 0 308 647" aria-hidden="true">
      <path d="M0 279 Q140 255 308 263 L308 647 L0 647 Z"/>
    </svg>

    <div class="intro">
      <h1>WIR SIND THERAPEUTEN<br>AUS <strong>ÜBERZEUGUNG</strong>!</h1>
      <p>Unsere Praxis gibt es <strong>seit 1969</strong>. In dieser Zeit konnten wir viel Erfahrung sammeln.</p>
      <p><strong>Wir</strong> sind ein Team aus älteren und jüngeren Therapeuten, aus Masseuren, med. Bade-<br>meistern und Physiotherapeuten. Diese bunte Mischung beinhaltet viel <strong>Erfahrung</strong> und viel <strong>Wissen</strong>. Beides wird in regelmäßigen internen Fortbildungen ausgetauscht. So ergänzen wir uns stets gegenseitig.</p>
      <p><strong>Wir</strong> arbeiten als Team <strong>Hand in Hand</strong> und schät-<br>zen das Fachwissen jedes einzelnen Kollegen.</p>
      <p><strong>Wir</strong> sind <strong>motiviert</strong> und mit <strong>Freude</strong> bei der Arbeit, denn wir wissen, was unsere Patienten mit Hilfe der Physiotherapie erreichen können.</p>
    </div>
  </section>

  <div class="thumb-strip">
    <!-- outside spread -->
    <div class="thumb blue" style="left:0;width:42px;">
      <h3>VIELZAHL VON THERAPIEMÖGLICH-KEITEN</h3>
      <div class="lines" style="top:24px;"><i></i><i></i><i></i><i class="short"></i><i></i><i></i><i></i><i></i><i class="short"></i></div>
      <div class="photo pool" role="img" aria-label="Foto: Bewegungsbad der Praxis"></div>
    </div>
    <div class="thumb white" style="left:42px;width:44px;">
      <h3>KONTAKT</h3>
      <div class="lines" style="top:17px;"><i class="short"></i><i></i><i></i><i class="short"></i><i></i><i class="short"></i><i class="short"></i></div>
      <div class="mini-mark faint" style="left:16px;top:74px;"></div>
    </div>
    <div class="thumb white" style="left:86px;width:45px;">
      <div class="mini-mark" style="left:17px;top:5px;"></div>
      <div class="mini-name" style="top:19px;">ZENTRUM FÜR THERAPIE &amp; TRAINING<br>Lena Vogt &amp; Tobias Kern</div>
      <div class="front-band">
        <div class="lines" style="top:4px;left:3px;"><i class="short"></i><i class="short"></i><i></i><i></i><i></i><i></i><i></i><i></i><i></i><i></i><i></i><i></i><i class="short"></i></div>
      </div>
    </div>

    <!-- inside spread -->
    <div class="thumb blue" style="left:135px;width:43px;">
      <h3>AKTIVES GESUND-HEITSTRAINING</h3>
      <div class="lines" style="top:17px;"><i></i><i></i><i></i><i class="short"></i><i></i><i></i></div>
      <div class="photo team" role="img" aria-label="Foto: Praxisteam in hellblauer Kleidung"></div>
      <div class="lines" style="top:68px;"><i></i><i></i><i></i><i></i><i class="short"></i></div>
    </div>
    <div class="thumb white" style="left:178px;width:44px;">
      <h3>ZIRKELTRAINING</h3>
      <div class="lines" style="top:17px;"><i></i><i></i><i></i><i class="short"></i><i></i><i></i><i></i><i class="short"></i></div>
      <div class="photo gym" role="img" aria-label="Foto: Trainingsgeräte im Gesundheitsstudio"></div>
    </div>
    <div class="thumb blue" style="left:222px;width:43px;">
      <h3>SO ERREICHEN SIE UNS!</h3>
      <div class="lines" style="top:19px;"><i></i><i></i><i class="short"></i><i></i><i></i><i class="short"></i><i></i><i></i><i class="short"></i><i></i><i class="short"></i><i class="short"></i><i class="short"></i></div>
    </div>
  </div>
  <div class="strip-label" style="left:526px;">AUSSEN</div>
  <div class="strip-label" style="left:663px;">INNEN</div>
</body>
</html>
```